Welding Fabrication and Inspection Business Card Design

Welding Fabrication and Inspection Services,

Business

Industrial Machinery ServicesMohammed Rahim30 Ballarat Street, Kellmore Heights.4122.QLD

```html
<!DOCTYPE html>
<html lang="en">
<head>
<meta charset="utf-8">
<title>Tarnwell Forge Services – Business Card</title>
<link href="https://fonts.googleapis.com/css2?family=Barlow:wght@500;600;700&family=Roboto:wght@400&display=swap" rel="stylesheet">
<style>
  :root {
    --backdrop: #a9a7a8;
    --card: #ffffff;
    --ink: #231f1e;
    --band: #2b2726;
    --stripe-grey: #8a8788;
    --tool-red: #9e2a35;
    --tool-dark: #3a3334;
  }
  * { margin: 0; padding: 0; box-sizing: border-box; }
  html, body { width: 1200px; height: 1200px; overflow: hidden; }
  body { background: var(--backdrop); position: relative; font-family: "Barlow", Arial, sans-serif; color: var(--ink); }

  .card { position: absolute; width: 714px; height: 420px; background: var(--card); overflow: hidden; }
  .card-front { left: 238px; top: 118px; }
  .card-back { left: 230px; top: 643px; height: 418px; }

  .brand { display: flex; align-items: center; gap: 12px; position: absolute; }
  .brand-mark { width: 16px; height: 16px; border-radius: 50%; background: var(--ink); flex: none; }
  .brand-name { font-weight: 600; color: var(--ink); white-space: nowrap; }

  .card-front .brand { left: 0; right: 0; top: 158px; justify-content: center; }
  .card-front .brand-name { font-size: 38px; }

  .service-band { position: absolute; left: 0; right: 0; bottom: 0; height: 72px; background: var(--band);
    display: flex; align-items: center; justify-content: center; }
  .service-band p { color: #fff; font-weight: 600; font-size: 24px; letter-spacing: 0.3px; }

  .back-shape { position: absolute; inset: 0; }

  .card-back .brand { left: 40px; top: 116px; }
  .card-back .brand-mark { width: 13px; height: 13px; }
  .card-back .brand-name { font-size: 27px; }

  .person { position: absolute; left: 39px; top: 200px; }
  .person-name { font-size: 28px; font-weight: 600; line-height: 1.1; }
  .person-role { font-size: 15px; font-weight: 600; margin-top: 4px; }

  .contact { position: absolute; left: 39px; top: 276px; font-family: "Roboto", Arial, sans-serif; font-size: 17px; line-height: 25px; list-style: none; }
  .contact li { display: flex; align-items: center; gap: 14px; }
  .contact svg { width: 18px; height: 14px; fill: var(--ink); flex: none; }
  .contact .address { display: block; margin-top: 2px; }

  .tool-photo { position: absolute; left: 528px; top: 276px; width: 180px; height: 118px; border-radius: 6px;
    background: linear-gradient(180deg, var(--tool-red) 0 45%, var(--tool-dark) 45% 100%); }
</style>
</head>
<body>

<section class="card card-front">
  <div class="brand">
    <span class="brand-mark"></span>
    <span class="brand-name">Tarnwell Forge Services</span>
  </div>
  <div class="service-band"><p>Welding Fabrication and Inspection Services</p></div>
</section>

<section class="card card-back">
  <svg class="back-shape" viewBox="0 0 714 418" preserveAspectRatio="none" aria-hidden="true">
    <path d="M486 0 C650 70 600 320 262 418 L714 418 L714 0 Z" fill="var(--stripe-grey)"/>
    <path d="M506 0 C672 72 626 322 296 418 L714 418 L714 0 Z" fill="#ffffff"/>
    <path d="M522 0 C690 76 646 326 322 418 L714 418 L714 0 Z" fill="var(--band)"/>
  </svg>

  <div class="brand">
    <span class="brand-mark"></span>
    <span class="brand-name">Tarnwell Forge Services</span>
  </div>

  <div class="person">
    <h1 class="person-name">Khalid Nasser</h1>
    <p class="person-role">Owner</p>
  </div>

  <ul class="contact">
    <li><svg viewBox="0 0 18 14"><path d="M1 4 C1 1 17 1 17 4 L15 6 L12 5 L12 3 L6 3 L6 5 L3 6 Z M4 7 L14 7 L16 13 L2 13 Z"/></svg>+00 444 555 6666</li>
    <li><svg viewBox="0 0 18 14"><path d="M1 1 H17 V13 H1 Z M2.5 2.5 L9 8 L15.5 2.5 V11.5 H2.5 Z" fill-rule="evenodd"/></svg>khalidnasser@tarnwellforge.com</li>
    <li class="address">17 Corrowen Street, Kellmore Heights<br>North. 7390. TVR</li>
  </ul>

  <div class="tool-photo" role="img" aria-label="Photo of a red magnetic particle inspection yoke with hinged legs"></div>
</section>

</body>
</html>
```